Information One Page for Email

I am looking for a informative attachment I can send with an introductive email for Ridgeview Cable Works. Something I can also Mail.

Ridgeview Cable Works is the leader in Rebar Post Tension Cable Placement and Post Tension Cable repair. Outside of cable placement and repair we do concrete repair, Parking Garage restoration and

Content

Post Tension Repair and Concrete Restoration
Post-tensioning is a revolutionary method in concrete construction that enhances the strength and durability of structures. However, like all construction ele-ments, post-tension cables can experience wear and damage over time. Ensuring timely and effective repair is crucial for maintaining the safety and integrity of your building.
Why Post-Tension Cable Repair is Essential
1. **Structural Integrity**: Damaged or deteriorated cables can compromise the structural integrity of your building, leading to safety hazards and potential structural failures.
2. **Extended Lifespan**: Regular maintenance and repair of post-tension cables extend the lifespan of your structure, ensuring it remains safe and function-al for years to come.
3. **Cost-Effective**: Addressing cable issues early on prevents more severe damage and costly repairs down the line.
Common Signs of Post-Tension Cable Issues
- Cracks in concrete surfaces
- Unusual noises or popping sounds
- Visible cable ends or broken strands
- Water leakage through cracks
Our Repair Process
1. **Inspection and Assessment**: Our team conducts a thorough inspection to identify the extent of the damage and determine the appropriate repair meth-ods.
2. **Cable Repair or Replacement**: Depending on the severity, we either re-pair the existing cables or replace them with new ones to restore full functional-ity.
3. **Sealing and Protection**: After repairing, we seal the affected areas to protect against moisture and future damage.
4. **Quality Assurance**: We perform rigorous quality checks to ensure the repairs meet industry standards and the structure is safe for use.
Why Choose Us
- **Expertise and Experience**: With years of experience in post-tension cable repair, our team is skilled in handling even the most complex repairs efficiently and effectively.
- **Advanced Technology**: We use the latest technology and materials to ensure durable and long-lasting repairs.
- **Customer Satisfaction**: Our commitment to quality and customer satisfaction sets us apart. We work closely with our clients to ensure their needs are met and expectations exceeded.
Contact Us
If you suspect issues with your post-tension cables or need a routine inspection, don't hesitate to contact us. Our experts are ready to provide the best solutions to keep your structures safe and secure.
Ensure the safety and longevity of your building with our professional post-tension cable repair services. Trust us to deliver quality and reliability every time.

```html
<!DOCTYPE html>
<html lang="en">
<head>
<meta charset="utf-8">
<title>Ridgeview Cable Works – Post Tension Repair</title>
<link href="https://fonts.googleapis.com/css2?family=Poppins:wght@400;500;600;700;800&family=Saira+Condensed:wght@700&family=Open+Sans:ital,wght@0,700;1,400;1,500&display=swap" rel="stylesheet">
<style>
:root{
  --backdrop:#8c8c8c;
  --paper:#ffffff;
  --green:#0b6b3a;
  --green-dark:#004d2a;
  --green-bright:#0a7a40;
  --mint:#dff2ea;
  --charcoal:#474747;
  --ink:#333333;
  --grey-head:#555555;
  --ring:#d9dcda;
}
*{margin:0;padding:0;box-sizing:border-box}
html,body{width:993px;height:1200px;overflow:hidden;background:var(--backdrop)}
body{font-family:"Poppins",sans-serif;color:var(--ink)}
.page{position:absolute;left:72px;top:73px;width:818px;height:1058px;background:var(--paper);overflow:hidden}
.abs{position:absolute}
.hero-band{left:0;top:0;width:818px;height:195px;background:linear-gradient(100deg,var(--green-dark) 30%,var(--green-bright) 70%,var(--green) 100%)}
.hero-photo{left:0;top:0}
.logo-panel{left:0;top:195px;width:330px;height:90px;background:rgba(240,242,242,.85);clip-path:polygon(0 0,300px 0,330px 45px,300px 90px,0 90px)}
.logo-name{left:52px;top:224px;font-family:"Poppins",sans-serif;font-weight:600;font-size:19px;color:var(--green);display:flex;align-items:center;gap:8px;letter-spacing:.2px}
.logo-name i{display:block;width:12px;height:12px;background:var(--green)}
.hero-title{left:383px;top:18px;font-family:"Saira Condensed","Arial Narrow",sans-serif;font-weight:700;font-size:38px;line-height:37px;color:#fff;white-space:nowrap;letter-spacing:.2px}
.hero-intro{left:383px;top:101px;width:384px;font-size:11px;line-height:13px;color:#fff;font-weight:500}
.why-title{left:48px;top:306px;font-weight:700;font-size:27px;line-height:33px;color:var(--grey-head)}
.pill{left:48px;width:269px;height:31px;border-radius:16px;background:linear-gradient(90deg,var(--green-dark),var(--green-bright));color:#fff;font-weight:700;font-size:19px;display:flex;align-items:center;gap:7px;padding-left:6px}
.tick{width:20px;height:20px;flex:none}
.why-text{left:48px;width:380px;font-size:13.6px;line-height:16px;color:var(--ink)}
.process-line{left:443px;width:2px;background:var(--green)}
.process-label{left:431px;top:583px;transform-origin:0 0;transform:rotate(-90deg);font-weight:700;font-size:21.5px;letter-spacing:.3px;color:var(--green);white-space:nowrap}
.step-head{left:600px;width:210px;font-weight:700;font-size:18px;line-height:21px;color:var(--green)}
.step-text{left:600px;width:198px;font-size:11.3px;line-height:13px;color:var(--ink)}
.signs-band{left:0;top:699px;width:818px;height:163px;background:var(--mint)}
.signs-title{left:53px;top:717px;font-weight:700;font-size:19px;line-height:23px;color:var(--green)}
.divider{top:720px;height:63px;border-left:1.5px dashed var(--green)}
.sign{top:722px;display:flex;gap:6px;font-size:14.5px;line-height:16px;color:var(--ink)}
.sign .tick{margin-top:1px}
.choose-box{left:47px;top:806px;width:730px;height:168px;border-radius:23px;background:var(--charcoal);overflow:hidden}
.choose-tab{left:47px;top:806px;width:256px;height:46px;background:linear-gradient(90deg,var(--green),var(--green-dark));border-radius:23px 0 23px 0;color:#fff;font-weight:700;font-size:25px;padding:2px 0 0 29px}
.choose-col{top:862px;color:#fff}
.choose-col h3{display:flex;align-items:center;gap:6px;font-weight:500;font-size:16.5px;margin-bottom:5px;white-space:nowrap}
.choose-col p{font-size:11.3px;line-height:13px;padding-left:3px}
.foot-note{left:50px;top:985px;width:450px;font-family:"Open Sans",sans-serif;font-style:italic;font-size:9.3px;line-height:11.5px;color:#222}
.foot-note.green{top:1012px;color:var(--green)}
.contact{left:523px;display:flex;align-items:center;gap:6px;font-family:"Open Sans",sans-serif;font-weight:700;font-size:16px;color:#222}
.contact svg{width:18px;height:18px}
</style>
</head>
<body>
<div class="page">
  <div class="abs hero-band"></div>
  <svg class="abs hero-photo" width="420" height="380" viewBox="0 0 420 380" role="img" aria-label="Photo of a concrete building with exposed post-tension cables under repair">
    <defs>
      <linearGradient id="photoTone" x1="0" y1="0" x2="1" y2="1">
        <stop offset="0" stop-color="#8f8f88"/><stop offset=".5" stop-color="#c9c6bd"/><stop offset="1" stop-color="#e9eef2"/>
      </linearGradient>
      <linearGradient id="fade" x1="0" y1="0" x2="0" y2="1">
        <stop offset="0" stop-color="#fff" stop-opacity="0"/><stop offset=".5" stop-color="#fff" stop-opacity="0"/><stop offset="1" stop-color="#fff" stop-opacity="1"/>
      </linearGradient>
    </defs>
    <polygon points="0,0 272,0 350,165 300,195 390,195 410,300 300,380 0,380" fill="url(#photoTone)"/>
    <rect x="0" y="180" width="420" height="200" fill="url(#fade)"/>
  </svg>
  <div class="abs logo-panel"></div>
  <div class="abs logo-name"><i></i>Ridgeview Cable Works</div>

  <h1 class="abs hero-title">Post Tension Repair and<br>Concrete Restoration</h1>
  <p class="abs hero-intro">Post-tensioning is a revolutionary method in concrete construction that enhances the strength and durability of structures. However, like all construction ele-ments, post-tension cables can experience wear and damage over time. Ensuring timely and effective repair is crucial for maintaining the safety and integrity of your building.</p>

  <h2 class="abs why-title">Why Post-Tension<br>Cable Repair is Essential</h2>

  <div class="abs pill" style="top:389px"><svg class="tick" viewBox="0 0 20 20"><circle cx="10" cy="10" r="10" fill="#fff"/><path d="M5.5 10.3l3 3 6-6.3" stroke="#0b6b3a" stroke-width="2.4" fill="none"/></svg>Structural Integrity</div>
  <p class="abs why-text" style="top:429px">Damaged or deteriorated cables can compromise the structural integrity of your building, leading to safety hazards and potential structural failures.</p>
  <div class="abs pill" style="top:488px"><svg class="tick" viewBox="0 0 20 20"><circle cx="10" cy="10" r="10" fill="#fff"/><path d="M5.5 10.3l3 3 6-6.3" stroke="#0b6b3a" stroke-width="2.4" fill="none"/></svg>Extended Lifespan</div>
  <p class="abs why-text" style="top:527px">Regular maintenance and repair of post-tension cables extend the lifespan of your structure, ensuring it remains safe and function-al for years to come.</p>
  <div class="abs pill" style="top:588px"><svg class="tick" viewBox="0 0 20 20"><circle cx="10" cy="10" r="10" fill="#fff"/><path d="M5.5 10.3l3 3 6-6.3" stroke="#0b6b3a" stroke-width="2.4" fill="none"/></svg>Cost-Effective</div>
  <p class="abs why-text" style="top:627px">Addressing cable issues early on prevents more severe damage and costly repairs down the line.</p>

  <div class="abs process-line" style="top:255px;height:70px"></div>
  <div class="abs process-line" style="top:590px;height:70px"></div>
  <div class="abs process-label">OUR REPAIR PROCESS</div>

  <svg class="abs" style="left:460px;top:220px" width="140" height="460" viewBox="0 0 140 460">
    <g fill="none" stroke="#bdbdbd" stroke-width="1.2">
      <path d="M110 46 A57 57 0 1 0 57 124"/>
      <path d="M57 124 A57 57 0 0 1 57 236"/>
      <path d="M57 236 A57 57 0 0 0 57 348"/>
      <path d="M57 348 A57 57 0 1 1 20 450"/>
    </g>
    <g fill="#0b6b3a"><circle cx="113" cy="46" r="3"/><circle cx="57" cy="124" r="3"/><circle cx="57" cy="348" r="3"/></g>
    <g fill="#555"><circle cx="57" cy="236" r="3"/><circle cx="20" cy="448" r="3"/></g>
    <g>
      <circle cx="67" cy="67" r="48" fill="var(--ring)"/><circle cx="67" cy="67" r="41" fill="#0b6b3a"/>
      <g stroke="#fff" stroke-width="2" fill="none"><circle cx="72" cy="62" r="14"/><path d="M62 72l-13 13"/><path d="M64 64l5-5 4 4 7-8"/></g>
    </g>
    <g>
      <circle cx="67" cy="180" r="48" fill="var(--ring)"/><circle cx="67" cy="180" r="41" fill="#555"/>
      <path d="M88 164H52a8 8 0 0 0 0 16h30a8 8 0 0 1 0 16H46" stroke="#fff" stroke-width="2.4" fill="none"/>
    </g>
    <g>
      <circle cx="67" cy="292" r="48" fill="var(--ring)"/><circle cx="67" cy="292" r="41" fill="#0b6b3a"/>
      <path d="M67 268l14 6v10c0 10-6 16-14 20-8-4-14-10-14-20v-10z" stroke="#fff" stroke-width="2" fill="none"/>
      <path d="M61 287l4 4 8-8" stroke="#fff" stroke-width="2" fill="none"/>
      <path d="M46 296c2 8 8 14 14 16M88 296c-2 8-8 14-14 16" stroke="#fff" stroke-width="2" fill="none"/>
    </g>
    <g>
      <circle cx="67" cy="401" r="48" fill="var(--ring)"/><circle cx="67" cy="401" r="41" fill="#555"/>
      <path d="M67 378l16 7v12c0 12-7 19-16 23-9-4-16-11-16-23v-12z" stroke="#fff" stroke-width="2" fill="none"/>
      <circle cx="67" cy="400" r="6" stroke="#fff" stroke-width="2" fill="none"/>
      <circle cx="87" cy="382" r="9" stroke="#fff" stroke-width="1.8" fill="#555"/>
      <path d="M83 382l3 3 5-5" stroke="#fff" stroke-width="1.8" fill="none"/>
    </g>
  </svg>

  <h3 class="abs step-head" style="top:231px">Inspection<br>and Assessment</h3>
  <p class="abs step-text" style="top:278px">Our team conducts a thorough inspection to identify the extent of the damage and determine the appropriate repair meth-ods.</p>
  <h3 class="abs step-head" style="top:346px">Cable Repair or<br>Replacement</h3>
  <p class="abs step-text" style="top:393px">Depending on the severity, we either re-pair the existing cables or replace them with new ones to restore full functional-ity.</p>
  <h3 class="abs step-head" style="top:464px">Sealing and<br>Protection</h3>
  <p class="abs step-text" style="top:511px">After repairing, we seal the affected areas to protect against moisture and future damage.</p>
  <h3 class="abs step-head" style="top:586px">Quality Assurance</h3>
  <p class="abs step-text" style="top:613px">We perform rigorous quality checks to ensure the repairs meet industry standards and the structure is safe for use.</p>

  <div class="abs signs-band"></div>
  <h2 class="abs signs-title">Common Signs<br>of Post-Tension<br>Cable Issues</h2>
  <div class="abs divider" style="left:223px"></div>
  <div class="abs divider" style="left:337px"></div>
  <div class="abs divider" style="left:486px"></div>
  <div class="abs divider" style="left:637px"></div>
  <div class="abs sign" style="left:235px"><svg class="tick" viewBox="0 0 20 20"><circle cx="10" cy="10" r="10" fill="#0b6b3a"/><path d="M5.5 10.3l3 3 6-6.3" stroke="#fff" stroke-width="2.2" fill="none"/></svg><span>Cracks in<br>concrete<br>surfaces</span></div>
  <div class="abs sign" style="left:350px"><svg class="tick" viewBox="0 0 20 20"><circle cx="10" cy="10" r="10" fill="#0b6b3a"/><path d="M5.5 10.3l3 3 6-6.3" stroke="#fff" stroke-width="2.2" fill="none"/></svg><span>Unusual noises<br>or popping<br>sounds</span></div>
  <div class="abs sign" style="left:499px"><svg class="tick" viewBox="0 0 20 20"><circle cx="10" cy="10" r="10" fill="#0b6b3a"/><path d="M5.5 10.3l3 3 6-6.3" stroke="#fff" stroke-width="2.2" fill="none"/></svg><span>Visible cable<br>ends or broken<br>strands</span></div>
  <div class="abs sign" style="left:649px"><svg class="tick" viewBox="0 0 20 20"><circle cx="10" cy="10" r="10" fill="#0b6b3a"/><path d="M5.5 10.3l3 3 6-6.3" stroke="#fff" stroke-width="2.2" fill="none"/></svg><span>Water leakage<br>through<br>cracks</span></div>

  <div class="abs choose-box"></div>
  <h2 class="abs choose-tab">Why Choose Us</h2>
  <div class="abs choose-col" style="left:71px;width:235px">
    <h3><svg class="tick" viewBox="0 0 20 20"><circle cx="10" cy="10" r="10" fill="#fff"/><path d="M5.5 10.3l3 3 6-6.3" stroke="#474747" stroke-width="2.4" fill="none"/></svg>Structural Integrity</h3>
    <p>With years of experience in post-tension cable repair, our team is skilled in handling even the most complex repairs efficiently and effectively.</p>
  </div>
  <div class="abs choose-col" style="left:326px;width:215px">
    <h3><svg class="tick" viewBox="0 0 20 20"><circle cx="10" cy="10" r="10" fill="#fff"/><path d="M5.5 10.3l3 3 6-6.3" stroke="#474747" stroke-width="2.4" fill="none"/></svg>Advanced Technology</h3>
    <p>We use the latest technology and materials to ensure durable and long-lasting repairs.</p>
  </div>
  <div class="abs choose-col" style="left:549px;width:215px">
    <h3><svg class="tick" viewBox="0 0 20 20"><circle cx="10" cy="10" r="10" fill="#fff"/><path d="M5.5 10.3l3 3 6-6.3" stroke="#474747" stroke-width="2.4" fill="none"/></svg>Customer Satisfaction</h3>
    <p>Our commitment to quality and customer satisfaction sets us apart. We work closely with our clients to ensure their needs are met and expectations exceeded.</p>
  </div>

  <p class="abs foot-note">If you suspect issues with your post-tension cables or need a routine inspection, don't hesitate to contact us. Our experts are ready to provide the best solutions to keep your structures safe and secure.</p>
  <p class="abs foot-note green">Ensure the safety and longevity of your building with our professional post-tension cable repair services. Trust us to deliver quality and reliability every time.</p>

  <div class="abs contact" style="top:986px"><svg viewBox="0 0 20 20"><circle cx="10" cy="10" r="10" fill="#0b6b3a"/><path d="M7 5l2 2.5-1.2 1.5c.8 1.6 1.7 2.5 3.2 3.2L12.5 11 15 13l-1 2c-4 0-8-4-8-8z" fill="#fff"/></svg>Call (555) 014-2290</div>
  <div class="abs contact" style="top:1009px"><svg viewBox="0 0 20 20"><circle cx="10" cy="10" r="10" fill="#0b6b3a"/><g stroke="#fff" stroke-width="1" fill="none"><circle cx="10" cy="10" r="6"/><ellipse cx="10" cy="10" rx="2.6" ry="6"/><path d="M4 10h12M5 7h10M5 13h10"/></g></svg>www.ridgeviewcableworks.com</div>
</div>
</body>
</html>
```